I need a header for the web site www.harlowspipeworks.example/demo
It must include the following
Existig Logo (I will upload the .png)
Text: Serving Calgary and Surrounding Areas for Over 30 Years!
24 Hour Service
Call 403.718.2946 (Note this isn't the actual phone number I will need to be able to change the Phone number once the site is ready to put in a tracking number so I am hoping I get a PSD file with this where the text is editable)
We wnat the feel to be warm and geared more towards a residential customer rather than an industial customer.
We would like blue tones but are open to anything warm.

Size: Aprroximately 960x300

• Rounded Corners to match the content area on the site

```html
<!DOCTYPE html>
<html lang="en">
<head>
<meta charset="utf-8">
<title>Harlow's Pipeworks Ltd — Header</title>
<link rel="stylesheet" href="https://fonts.googleapis.com/css2?family=Libre+Baskerville:wght@700&family=Oswald:wght@600&display=swap">
<style>
  :root {
    --page: #ffffff;
    --aqua: #00f0ff;
    --aqua-edge: #00c6dc;
    --aqua-light: #7ff8ff;
    --ink: #000000;
  }
  html, body {
    margin: 0;
    width: 1200px;
    height: 1200px;
    overflow: hidden;
    background: var(--page);
  }
  .canvas {
    position: relative;
    width: 1200px;
    height: 1200px;
  }
  .header-banner {
    position: absolute;
    left: 45px;
    top: 22px;
    width: 918px;
    height: 296px;
    border-radius: 8px;
    background: var(--aqua);
    box-shadow: inset 0 0 0 2px var(--aqua-edge), inset 3px 3px 6px var(--aqua-light);
  }
  .header-panel {
    position: absolute;
    left: 18px;
    top: 25px;
    width: 884px;
    height: 248px;
    border-radius: 4px;
    background: var(--aqua);
    box-shadow: inset 2px 2px 3px var(--aqua-edge), 2px 2px 2px var(--aqua-light), -1px -1px 2px var(--aqua-edge);
  }
  .brand {
    position: absolute;
    left: 60px;
    top: 105px;
    width: 420px;
    text-align: center;
    font-family: "Libre Baskerville", Georgia, serif;
    font-weight: 700;
    font-size: 24px;
    letter-spacing: 1px;
    color: var(--ink);
  }
  .service-hours {
    position: absolute;
    left: 560px;
    top: 50px;
    margin: 0;
    font-family: "Oswald", "Arial Narrow", sans-serif;
    font-weight: 600;
    font-size: 52px;
    line-height: 1;
    letter-spacing: -1px;
    color: var(--ink);
    transform: scaleX(0.92);
    transform-origin: left;
  }
  .call-line {
    position: absolute;
    left: 560px;
    top: 150px;
    margin: 0;
    font-family: "Libre Baskerville", Georgia, serif;
    font-weight: 700;
    font-size: 27px;
    color: var(--ink);
  }
  .tagline {
    position: absolute;
    left: 14px;
    top: 230px;
    width: 856px;
    margin: 0;
    text-align: center;
    font-family: "Libre Baskerville", Georgia, serif;
    font-weight: 700;
    font-size: 21px;
    letter-spacing: 0.6px;
    color: var(--ink);
  }
</style>
</head>
<body>
<div class="canvas">
  <header class="header-banner">
    <div class="header-panel"></div>
    <div class="brand">HARLOW'S PIPEWORKS LTD</div>
    <h1 class="service-hours">24 Hour Service</h1>
    <p class="call-line">Call 403.718.2946</p>
    <p class="tagline">Serving Calgary and Surrounding Areas for Over 30 Years</p>
  </header>
</div>
</body>
</html>
```